Rota sem falha

We need a web design for a new company based in João Pessoa, Brazil, called Rota Sem Falha (Smooth Route). After the client/consumer fullfill a questionary about the wanted destination, personal interests and available budget for the trip, we aim to plan a personalized travel guide for that independent travellers, containing informations about the places we suggest them to visit, amount of days indicated in each city, possibles restaurants and hotels. The site will help people to manage their budgets and optimize the time at their travel at a low cost and in a simple way. We would like to see clean and sophisticated design that use colors in shades of black, grey and white (and perhaps a touch of pink - what do you think?). The final design should communicate safety, professionalism and experience.
Updates
Target Market(s)
People who dont like to buy excursion packages but think they could need a consultance in planning their trip
Industry/Entity Type
It Company
Requirements
Must have
- The menu shall indicate the following points (that will lead to new pages):
1-Our Services
2-Prices
2- FAQ
3-Hire a travel expert to plan your trip!
4-Around the world - blog
Fell free to put the logo of the site "Rota Sem Falha" in the top middle/top left/ or wherever you find it is more appropriate.
On the top right we should put a login/register button.
Above that menu, I thought about illustrating with a figure demonstrating how it works - step by step, as seen in the link http://trekvolo.example/ - but in a more clean design.
Nice to have
- Quik coin will be used as the payment option.

```html
<!DOCTYPE html>
<html lang="en">
<head>
<meta charset="utf-8">
<title>Rota Sem Falha — Plan your Trip</title>
<link rel="stylesheet" href="https://fonts.googleapis.com/css2?family=PT+Sans:ital,wght@0,400;0,700;1,400&family=Roboto+Condensed:wght@400;700&family=Arimo:ital,wght@0,400;0,700;1,400&display=swap">
<style>
  :root{
    --pink:#ec1a8c;
    --header:#3d3d3f;
    --ink:#3a3a3a;
    --body:#555;
    --muted:#7a7a7a;
    --paper:#efeeee;
    --white:#fff;
    --footer:#1c1c1c;
    --step:#6b6b6b;
  }
  html,body{margin:0;padding:0;overflow:hidden;}
  body{width:952px;height:1200px;background:var(--white);}
  .page{position:relative;width:952px;height:1200px;overflow:hidden;font-family:"Arimo",Arial,sans-serif;color:var(--body);}
  .abs{position:absolute;}

  /* header */
  .header{left:0;top:0;width:952px;height:114px;background:var(--header);border-top:2px solid var(--pink);box-sizing:border-box;}
  .brand{left:104px;top:34px;font-family:"PT Sans",sans-serif;font-weight:700;font-size:34px;color:var(--white);letter-spacing:.3px;display:flex;align-items:center;gap:8px;}
  .brand-dot{width:10px;height:10px;background:var(--pink);border-radius:50%;}
  .account{left:704px;top:0;width:124px;height:26px;}
  .account-links{left:704px;top:0;width:124px;height:26px;display:flex;align-items:center;justify-content:center;gap:7px;font-family:"Arimo",sans-serif;font-size:10.5px;color:var(--white);}
  .started{left:413px;top:15px;font-family:"PT Sans",sans-serif;font-size:17px;color:var(--white);}
  .steps{left:414px;top:44px;width:416px;height:54px;}
  .step-label{position:absolute;top:10px;width:70px;text-align:center;color:var(--white);font-family:"Roboto Condensed",sans-serif;}
  .step-label b{display:block;font-size:15.5px;font-weight:700;line-height:16px;}
  .step-label span{display:block;font-family:"Arimo",sans-serif;font-size:9px;line-height:14px;color:#eee;}

  /* nav */
  .nav{left:0;top:114px;width:952px;height:41px;background:linear-gradient(#fff,#e2e2e2);border-bottom:1px solid #b9b9b9;box-sizing:border-box;}
  .nav a{position:absolute;top:12px;font-family:"Roboto Condensed",sans-serif;font-size:13.5px;color:#333;text-decoration:none;}
  .nav i{position:absolute;top:10px;width:1px;height:22px;background:#cfcfcf;}

  /* slider */
  .stage{left:0;top:155px;width:952px;height:412px;background:var(--paper);}
  .frame{left:110px;top:171px;width:730px;height:347px;background:var(--white);border:1px solid #e2e2e2;box-sizing:border-box;box-shadow:0 6px 10px -6px rgba(0,0,0,.25);}
  .hero-photo{left:118px;top:179px;width:712px;height:330px;background:linear-gradient(180deg,#5a5a5c 0%,#8e8e90 45%,#4a4a4b 80%,#2b2b2c 100%);}
  .hero-band{left:536px;top:331px;width:294px;height:77px;background:rgba(255,255,255,.45);}
  .hero-title{right:144px;top:334px;font-family:"PT Sans",sans-serif;font-weight:700;font-size:42px;color:#333;letter-spacing:.5px;}
  .hero-sub{right:150px;top:383px;font-family:"PT Sans",sans-serif;font-style:italic;font-size:14.5px;color:var(--pink);}
  .hero-btn{left:587px;top:432px;width:219px;height:45px;border-radius:23px;background:linear-gradient(#fff,#d9d9d9);box-shadow:0 2px 4px rgba(0,0,0,.4);font-family:"PT Sans",sans-serif;font-weight:700;font-size:21px;color:#333;display:flex;align-items:center;justify-content:center;letter-spacing:.4px;}
  .pager{left:396px;top:536px;width:150px;height:22px;}

  /* content */
  .h2{font-family:"PT Sans",sans-serif;font-weight:700;font-size:27px;color:var(--ink);margin:0;}
  .overview-title{left:113px;top:593px;}
  .overview-copy{left:113px;top:640px;width:445px;font-size:10.5px;line-height:16px;text-align:justify;color:var(--body);}
  .overview-copy p{margin:0 0 16px;}
  .work-title{left:582px;top:593px;}
  .video{left:582px;top:637px;width:250px;height:179px;border:1px solid #ddd;box-sizing:border-box;background:#f6f6f6;}
  .video-still{left:587px;top:643px;width:239px;height:167px;background:linear-gradient(135deg,#8a8a8a,#c9c9c9 50%,#6f6f6f);}
  .play{left:680px;top:700px;width:48px;height:48px;}

  .testi-title{left:0;top:862px;width:922px;text-align:center;}
  .rule{top:878px;height:5px;background:repeating-linear-gradient(135deg,#ddd 0 1px,#fff 1px 3px);}
  .testi-copy{left:190px;top:915px;width:542px;text-align:center;font-size:10.5px;line-height:21px;color:var(--muted);}
  .testi-name{left:380px;top:988px;width:160px;text-align:center;font-size:10.5px;font-weight:700;color:#222;letter-spacing:.3px;}
  .testi-arrows{left:348px;top:985px;width:220px;height:20px;}

  .news{left:115px;top:1026px;width:689px;height:73px;background:#f7f7f7;border:1px solid #efefef;box-sizing:border-box;}
  .quote-mark{left:140px;top:1040px;font-family:"PT Sans",serif;font-size:50px;line-height:50px;color:#bbb;}
  .quote-copy{left:178px;top:1047px;width:340px;font-style:italic;font-size:10px;line-height:16px;color:#999;}
  .news-divider{left:542px;top:1039px;width:1px;height:48px;background:#ddd;}
  .email{left:558px;top:1053px;width:154px;height:21px;background:var(--white);border:1px solid #eee;box-sizing:border-box;font-style:italic;font-size:7.5px;color:#aaa;padding-left:8px;line-height:19px;}
  .submit{left:713px;top:1053px;width:54px;height:21px;background:#1a1a1a;color:var(--white);font-size:8px;font-weight:700;display:flex;align-items:center;justify-content:center;}

  /* footer */
  .footer{left:0;top:1120px;width:952px;height:80px;background:var(--footer);}
  .foot-links{left:118px;top:1144px;font-size:10.5px;color:#ddd;word-spacing:1px;}
  .foot-links span{margin:0 9px;}
  .copyright{left:118px;top:1164px;font-size:10.5px;color:#ddd;}
  .seal{left:648px;top:1138px;width:48px;height:48px;border-radius:50%;background:radial-gradient(circle at 40% 35%,#f6dc7a,#d4a928);}
  .pay-name{left:728px;top:1138px;font-family:"PT Sans",sans-serif;font-weight:700;font-size:17px;color:var(--white);}
  .cards{left:707px;top:1170px;display:flex;gap:3px;}
  .cards i{display:block;width:25px;height:15px;background:#d8d8d8;border-radius:2px;}
</style>
</head>
<body>
<div class="page">

  <header class="abs header"></header>
  <div class="abs brand"><span>Rota Sem Falha</span><span class="brand-dot"></span></div>

  <svg class="abs account" viewBox="0 0 124 26" aria-hidden="true"><polygon points="0,0 124,0 116,26 8,26" fill="var(--pink)"/></svg>
  <div class="abs account-links"><span>Login</span><span>|</span><span>Register</span></div>

  <div class="abs started">Get Started Now!</div>
  <svg class="abs steps" viewBox="0 0 416 54" aria-hidden="true">
    <defs>
      <linearGradient id="stepFill" x1="0" y1="0" x2="0" y2="1">
        <stop offset="0" stop-color="#7a7a7a"/><stop offset="1" stop-color="#5c5c5c"/>
      </linearGradient>
    </defs>
    <polygon points="0,0 70,0 90,27 70,54 0,54" fill="url(#stepFill)"/>
    <polygon points="70,0 152,0 172,27 152,54 70,54 90,27" fill="url(#stepFill)" stroke="#4a4a4a" stroke-width="1"/>
    <polygon points="152,0 234,0 254,27 234,54 152,54 172,27" fill="url(#stepFill)" stroke="#4a4a4a" stroke-width="1"/>
    <polygon points="234,0 316,0 336,27 316,54 234,54 254,27" fill="url(#stepFill)" stroke="#4a4a4a" stroke-width="1"/>
    <polygon points="316,0 396,0 416,27 396,54 316,54 336,27" fill="url(#stepFill)" stroke="#4a4a4a" stroke-width="1"/>
  </svg>
  <div class="abs step-label" style="left:416px;top:54px"><b>Generate</b><span>dummy text</span></div>
  <div class="abs step-label" style="left:502px;top:54px"><b>Review</b><span>dummy text</span></div>
  <div class="abs step-label" style="left:586px;top:54px"><b>Date</b><span>dummy text</span></div>
  <div class="abs step-label" style="left:667px;top:54px"><b>Trip</b><span>dummy text</span></div>
  <div class="abs step-label" style="left:749px;top:54px"><b>Compare</b><span>dummy text</span></div>

  <nav class="abs nav">
    <a style="left:113px">Home</a><i style="left:168px"></i>
    <a style="left:190px">Our Services</a><i style="left:282px"></i>
    <a style="left:304px">Prices</a><i style="left:361px"></i>
    <a style="left:384px">FAQ</a><i style="left:428px"></i>
    <a style="left:451px">Hire a travel expert</a><i style="left:580px"></i>
    <a style="left:600px">Around the world - blog</a><i style="left:750px"></i>
    <a style="left:773px">Contact Us</a>
  </nav>

  <section class="abs stage"></section>
  <div class="abs frame"></div>
  <div class="abs hero-photo" role="img" aria-label="Black and white night photo of a historic bascule bridge with gothic towers"></div>
  <div class="abs hero-band"></div>
  <div class="abs hero-title">Plan your Trip</div>
  <div class="abs hero-sub">with expert consultants</div>
  <div class="abs hero-btn">Get Started Now!</div>

  <svg class="abs pager" viewBox="0 0 150 22" aria-hidden="true">
    <polyline points="14,3 6,11 14,19" fill="none" stroke="#bbb" stroke-width="3"/>
    <circle cx="36" cy="11" r="9" fill="#777"/>
    <circle cx="60" cy="11" r="9" fill="var(--pink)"/>
    <circle cx="84" cy="11" r="9" fill="#777"/>
    <circle cx="108" cy="11" r="9" fill="#777"/>
    <polyline points="134,3 142,11 134,19" fill="none" stroke="#bbb" stroke-width="3"/>
  </svg>

  <h2 class="abs h2 overview-title">Overview !</h2>
  <div class="abs overview-copy">
    <p>Praesent vestibulum molestie lacus. Aenean nonummy hendrerit mauris. Phasellus porta. Fusce suscipit varius mi. Cum sociis natoque penatibus et magnis dis parturient montes, nascetur ridiculus mus. Nulla dui. Fusce feugiat malesuada odio. Morbi nunc odio, gravida at, cursus nec, luctus a, lorem. Maecenas tristique orci ac sem. Duis ultricies montes, nascetur ridiculus mus. Nulla dui. Fusce feugiat malesuada odio. Morbi nunc odio, gravida at, cursus nec, luctus a, lorem. Maecenas tristique orci ac sem. Duis ultricies pharetra magna. Donec accumsan malesuada orci.</p>
    <p>Montes, nascetur ridiculus mus. Nulla dui. Fusce feugiat malesuada odio. Morbi nunc odio, gravida at, cursus nec, luctus a, lorem. Maecenas tristique orci ac sem. Duis ultricies montes, nascetur ridiculus mus. Nulla dui.</p>
  </div>

  <h2 class="abs h2 work-title">How We Work?</h2>
  <div class="abs video"></div>
  <div class="abs video-still" role="img" aria-label="Video still of travel consultants reviewing a plan with a client at a desk"></div>
  <svg class="abs play" viewBox="0 0 48 48" aria-hidden="true">
    <circle cx="24" cy="24" r="23" fill="rgba(0,0,0,.35)"/>
    <polygon points="18,13 36,24 18,35" fill="rgba(255,255,255,.85)"/>
  </svg>

  <div class="abs rule" style="left:116px;width:238px"></div>
  <div class="abs rule" style="left:566px;width:238px"></div>
  <h2 class="abs h2 testi-title">Testimonials</h2>
  <div class="abs testi-copy">At vero eos et accusamus et iusto odio dignissimos ducimus qui blanditiis praesentium voluptatum deleniti atque corrupti quos dolores et quas molestias excepturi sint occaecati cupiditate non provident, similique sunt in culpa qui officia deserunt mollitia animi, id est laborum...</div>
  <svg class="abs testi-arrows" viewBox="0 0 220 20" aria-hidden="true">
    <polyline points="10,3 3,10 10,17" fill="none" stroke="#222" stroke-width="2"/>
    <polyline points="212,3 219,10 212,17" fill="none" stroke="#222" stroke-width="2"/>
  </svg>
  <div class="abs testi-name">Lena Prado, Recife</div>

  <div class="abs news"></div>
  <div class="abs quote-mark">&ldquo;</div>
  <div class="abs quote-copy">At vero eos et accusamus et iusto odio dignimos ducimus qui blanditiis praese ntium voluptatum deleniti atque. Errupti quos dolores et quas...</div>
  <div class="abs news-divider"></div>
  <div class="abs email">YOUR E-MAIL</div>
  <div class="abs submit">SUBMIT</div>

  <footer class="abs footer"></footer>
  <div class="abs foot-links">Home<span>|</span>Our Services<span>|</span>Prices<span>|</span>FAQ<span>|</span>Hire a travel expert<span>|</span>Blog</div>
  <div class="abs copyright">Copyright © Rota Sem Falha&nbsp; 2013&nbsp; All Rights Reserved</div>
  <div class="abs seal"></div>
  <div class="abs pay-name">Quik coin</div>
  <div class="abs cards"><i></i><i></i><i></i><i></i></div>

</div>
</body>
</html>
```